Web design and optimisation

We are merging with another company. We require the following pages to be incorporated into our website but with a consistent look and feel and a general tidy up of our entire website. It needs to be optimised for web and mobile viewing and we want more hits on the site.

Our existing site needs some tidying up. We like a fresh, clean, contemporary and professional look.

Our current site:
kestrelview audits.com.au
The site that needs to be merged is bramblewoodhomeinspect.com.au
We only need the pages that relate to the "termite services" and and "pest control"

```html
<!DOCTYPE html>
<html lang="en">
<head>
<meta charset="utf-8">
<title>Kestrelview Audits – Certification &amp; Presale Reports</title>
<link href="https://fonts.googleapis.com/css2?family=Lato:ital,wght@0,400;0,700;0,900;1,400&display=swap" rel="stylesheet">
<style>
:root{
  --blue:#1a7bc4;
  --navy:#1d3a8c;
  --teal:#16917f;
  --ink:#222;
  --muted:#444;
  --card:#f0f1f4;
  --dark:#151619;
  --white:#fff;
}
*{box-sizing:border-box;margin:0;padding:0}
html,body{width:1200px;height:4141px;overflow:hidden}
body{font-family:'Lato',sans-serif;color:var(--ink);background:var(--white);position:relative}
.abs{position:absolute}
.btn{position:absolute;display:flex;align-items:center;justify-content:center;background:var(--teal);color:#fff;font-weight:700;font-size:14px;letter-spacing:.5px;text-transform:uppercase;width:150px;height:47px}
.btn-outline{background:transparent;border:2px solid #fff}

/* header */
.brand{left:85px;top:36px;font-size:24px;font-weight:700;color:var(--navy)}
.brand-mark{display:inline-block;width:16px;height:16px;background:var(--blue);margin-right:8px;vertical-align:middle}
.contact-top{top:30px;right:72px;display:flex;gap:22px;align-items:center;color:var(--navy);font-weight:700}
.contact-top .item{display:flex;align-items:center;gap:10px}
.contact-top .circle{width:38px;height:38px;border-radius:50%;background:var(--teal);display:flex;align-items:center;justify-content:center}
.contact-top .phone{font-size:24px}
.contact-top .mail{font-size:17px}
.nav{top:98px;left:0;width:1200px;height:59px;background:var(--blue);display:flex;justify-content:center;align-items:center;gap:26px}
.nav a{color:#fff;text-decoration:none;font-size:14px;font-weight:700;letter-spacing:.3px}

/* hero */
.hero{top:157px;left:0;width:1200px;height:628px;background:linear-gradient(100deg,#eef0ec 0%,#d9ddd6 45%,#2a3550 75%,#1a2538 100%);clip-path:polygon(0 0,100% 0,100% 100%,0 86.5%)}
.hero-title{left:74px;top:322px;font-size:63px;font-weight:900;color:var(--navy);line-height:.95;text-transform:uppercase}
.hero-sub{left:76px;top:462px;font-size:32px;font-weight:700;color:#111}
.dots{left:74px;top:638px;display:flex;gap:6px}
.dots span{width:36px;height:5px;background:#bbb}
.dots span.on{background:var(--blue)}

/* about */
.frame{background:var(--navy)}
.photo{background:linear-gradient(135deg,#8a6a4a,#c9a98a 50%,#5a4633)}
.sec-title{font-size:34px;font-weight:900;color:#111;text-transform:uppercase;white-space:nowrap}
.body-text{font-size:14px;line-height:28px;color:var(--ink)}

/* services */
.band-blue{background:var(--blue)}
.svc-card{background:var(--card);width:513px;height:465px}
.svc-img{height:236px;width:100%}
.svc-card h3{margin:24px 0 0 25px;font-size:31px;font-weight:900;color:var(--navy);text-transform:uppercase}
.svc-card p{margin:8px 50px 0 25px;font-size:14.5px;line-height:27px}

/* why */
.center-title{left:0;width:1200px;text-align:center;font-size:33px;font-weight:900;color:#222;text-transform:uppercase}
.why-card{width:243px;height:197px;background:var(--card);box-shadow:0 4px 12px rgba(0,0,0,.18);text-align:center;padding-top:82px;font-size:19px;font-weight:700;color:var(--navy);line-height:28px}
.why-icon{width:96px;height:96px;border-radius:50%;background:var(--teal);display:flex;align-items:center;justify-content:center}

/* testimonial */
.quote{left:190px;width:820px;text-align:center;font-size:22px;font-style:italic;color:#fff;line-height:38px}
.quote-name{left:0;width:1200px;text-align:center;font-size:16px;font-weight:900;color:#fff}

/* partners */
.partners{top:2950px;left:74px;display:flex;gap:10px}
.partner{width:168px;height:98px;border:1px solid #ccc;display:flex;align-items:center;justify-content:center;font-size:22px;font-weight:700;color:var(--ink)}

/* footer */
.foot-h{font-size:18px;font-weight:700;color:#fff;text-transform:uppercase}
.foot-list{font-size:13px;color:#ddd;line-height:31px;list-style:none}
.badge{background:#fff}
.copy{left:76px;top:4104px;font-size:12px;color:#ddd}
.social{right:72px;top:4098px;display:flex;gap:18px}
.social span{width:20px;height:20px;border-radius:50%;background:var(--blue)}
</style>
</head>
<body>

<header>
  <div class="abs brand"><span class="brand-mark"></span>Kestrelview Audits</div>
  <div class="abs contact-top">
    <div class="item"><span class="circle"><svg width="18" height="18" viewBox="0 0 24 24"><path fill="#fff" d="M6.6 10.8a15 15 0 0 0 6.6 6.6l2.2-2.2c.3-.3.7-.4 1-.2 1.1.4 2.3.6 3.6.6.6 0 1 .4 1 1V20c0 .6-.4 1-1 1A17 17 0 0 1 3 4c0-.6.4-1 1-1h3.5c.6 0 1 .4 1 1 0 1.3.2 2.5.6 3.6.1.3 0 .7-.2 1z"/></svg></span><span class="phone">02 6140 0375</span></div>
    <div class="item"><span class="circle"><svg width="18" height="14" viewBox="0 0 24 18"><rect width="24" height="18" rx="2" fill="#fff"/><path d="M1 2l11 8 11-8" stroke="#16917f" stroke-width="2" fill="none"/></svg></span><span class="mail">info@kestrelviewaudits.com.au</span></div>
  </div>
  <nav class="abs nav">
    <a>HOME</a><a>BOOK</a><a>BUILDING REPORTS</a><a>PEST MANAGEMENT</a><a>CERTIFICATION</a><a>PRICING</a><a>EXPLORE</a><a>CHARITY</a><a>ABOUT</a><a>CONTACT</a>
  </nav>
</header>

<section>
  <div class="abs hero" role="img" aria-label="Inspector in a kitchen holding a handheld moisture meter"></div>
  <h1 class="abs hero-title">Certification<br>&amp; Presale Reports</h1>
  <p class="abs hero-sub">Straightforward, time sensitive approach</p>
  <a class="btn" style="left:74px;top:523px">Read More</a>
  <div class="abs dots"><span class="on"></span><span></span><span></span></div>
</section>

<section>
  <div class="abs frame" style="left:72px;top:860px;width:505px;height:402px"></div>
  <div class="abs photo" style="left:82px;top:872px;width:505px;height:400px" role="img" aria-label="Inspector with a torch in a roof space"></div>
  <h2 class="abs sec-title" style="left:614px;top:935px">About Kestrelview Audits</h2>
  <p class="abs body-text" style="left:614px;top:986px;width:495px">Canberra's premier presale building and pest inspection service - we conduct more inspections than any other company in the region and take enormous pride on unsurpassed turnaround, outstanding customer service and presale reports that deliver the absolute best outcome for sellers and buyers.</p>
  <a class="btn" style="left:614px;top:1152px">Read More</a>
</section>

<section>
  <svg class="abs" style="left:0;top:1330px" width="1200" height="662"><polygon points="0,65 870,3 1200,90 1200,662 0,662" fill="#1a7bc4"/></svg>
  <article class="abs svc-card" style="left:74px;top:1461px">
    <div class="svc-img" style="background:linear-gradient(135deg,#6d5e52,#e4e6ea 55%,#a9b6c4)" role="img" aria-label="Two technicians in protective suits reviewing a tablet"></div>
    <h3>Termite Services</h3>
    <p>Nam vehicula pharetra mi, a varius nisl rhoncus volutpat.nunc quis lobortis nisl. Donec sit amet tortor eu tellus ultricies tempus sed quis augue.</p>
    <a class="btn" style="left:25px;top:391px">Read More</a>
  </article>
  <article class="abs svc-card" style="left:613px;top:1461px">
    <div class="svc-img" style="background:linear-gradient(135deg,#8f9aa5,#e8eaee 55%,#4d5968)" role="img" aria-label="Technician in protective suit spraying along a skirting board"></div>
    <h3>Pest Control</h3>
    <p>Nam vehicula pharetra mi, a varius nisl rhoncus volutpat.nunc quis lobortis nisl. Donec sit amet tortor eu tellus ultricies tempus sed quis augue.</p>
    <a class="btn" style="left:25px;top:391px">Read More</a>
  </article>
</section>

<section>
  <h2 class="abs center-title" style="top:2062px">Why Choose Us?</h2>
  <svg class="abs" style="left:0;top:2170px" width="1200" height="580"><polygon points="0,150 1200,15 1200,580 0,580" fill="#16917f"/></svg>
  <div class="abs why-card" style="left:74px;top:2183px">We've been around<br>the longest.</div>
  <div class="abs why-card" style="left:345px;top:2183px">We've done more<br>inspections.</div>
  <div class="abs why-card" style="left:614px;top:2183px">Our turnaround and<br>quality is unsurpassed.</div>
  <div class="abs why-card" style="left:885px;top:2183px">Buyers want our<br>reports.</div>
  <div class="abs why-icon" style="left:147px;top:2137px"><svg width="36" height="36" viewBox="0 0 24 24" fill="none" stroke="#fff" stroke-width="2.2"><circle cx="12" cy="12" r="10"/><path d="M12 6v6l4 2"/></svg></div>
  <div class="abs why-icon" style="left:418px;top:2137px"><svg width="36" height="36" viewBox="0 0 24 24" fill="none" stroke="#fff" stroke-width="2.2"><circle cx="12" cy="12" r="10"/><path d="M7 12l3 3 7-7"/></svg></div>
  <div class="abs why-icon" style="left:687px;top:2137px"><svg width="36" height="36" viewBox="0 0 24 24" fill="none" stroke="#fff" stroke-width="2"><path d="M3 10h4v11H3zM7 20h10l3-8v-2h-7l1-5-2-1-5 7"/></svg></div>
  <div class="abs why-icon" style="left:958px;top:2137px"><svg width="36" height="36" viewBox="0 0 24 24" fill="none" stroke="#fff" stroke-width="2.2"><path d="M3 3v18h18M8 17v-5M12 17V8M16 17v-7M20 17v-3"/></svg></div>

  <h2 class="abs center-title" style="top:2462px;color:#fff">Our Customers Say</h2>
  <p class="abs quote" style="top:2528px">I chose Kestrelview Audits because of their local charity program, they were fast, professional and reasonably priced. I would not hesitate to recommend them to a friend and I will definitely be using them again next time.</p>
  <p class="abs quote-name" style="top:2660px">DANIEL, ASHGROVE</p>
  <svg class="abs" style="left:58px;top:2578px" width="20" height="36"><path d="M16 2L3 18l13 16" stroke="#fff" stroke-width="3" fill="none"/></svg>
  <svg class="abs" style="left:1120px;top:2578px" width="20" height="36"><path d="M4 2l13 16L4 34" stroke="#fff" stroke-width="3" fill="none"/></svg>
</section>

<section>
  <h2 class="abs center-title" style="top:2812px">We Work With The Best</h2>
  <p class="abs" style="left:140px;top:2866px;width:920px;text-align:center;font-size:14px;line-height:28px">We are fortunate to have Australia's best real estate agents and conveyancing solicitors right on our doorstep. Click on the links below to head to the websites of some seriously talented experts that we work with every day.</p>
  <svg class="abs" style="left:40px;top:2982px" width="16" height="34"><path d="M14 2L3 17l11 15" stroke="#555" stroke-width="2.5" fill="none"/></svg>
  <div class="abs partners">
    <div class="partner">Northgate</div>
    <div class="partner">Westbrook</div>
    <div class="partner">Halloran</div>
    <div class="partner">Tarrant</div>
    <div class="partner">Fenwick</div>
    <div class="partner">Quillon</div>
  </div>
  <svg class="abs" style="left:1142px;top:2982px" width="16" height="34"><path d="M2 2l11 15L2 32" stroke="#555" stroke-width="2.5" fill="none"/></svg>
</section>

<section>
  <div class="abs band-blue" style="left:0;top:3140px;width:1200px;height:680px"></div>
  <div class="abs frame" style="left:72px;top:3222px;width:505px;height:398px"></div>
  <div class="abs photo" style="left:82px;top:3222px;width:505px;height:400px;background:linear-gradient(135deg,#e6e2dc,#c7ccd4 55%,#6c6a6e)" role="img" aria-label="Two women at an office desk with a computer"></div>
  <h2 class="abs sec-title" style="left:614px;top:3280px;color:#fff">Safe Harbour</h2>
  <p class="abs body-text" style="left:614px;top:3330px;width:510px;color:#fff">Every year we step into hundreds of homes across the city, yet in Canberra there are still so many people living without acceptable, permanent or safe shelter. Whilst we commit our resources to many charities throughout the year, our in-house program 'Safe Harbour' focuses on supporting members of our community who do not have a place to call home.</p>
  <a class="btn btn-outline" style="left:614px;top:3498px">Read More</a>
  <div class="abs" style="left:948px;top:3582px;font-size:28px;font-weight:700;color:#fff">Safe Harbour</div>
</section>

<footer>
  <svg class="abs" style="left:0;top:3695px" width="1200" height="446"><polygon points="0,95 1200,0 1200,446 0,446" fill="#151619"/></svg>
  <h3 class="abs foot-h" style="left:80px;top:3815px">Site Map</h3>
  <ul class="abs foot-list" style="left:80px;top:3845px"><li>Home</li><li>Book</li><li>Building Reports</li><li>Pest Management</li><li>Certification</li><li>Pricing</li></ul>
  <ul class="abs foot-list" style="left:242px;top:3845px"><li>Explore</li><li>Charity</li><li>About</li><li>Contact</li></ul>
  <h3 class="abs foot-h" style="left:420px;top:3815px">Contact Info</h3>
  <ul class="abs foot-list" style="left:420px;top:3845px;line-height:28px">
    <li><svg width="10" height="14" viewBox="0 0 10 14" style="margin-right:20px"><path d="M5 0a5 5 0 0 1 5 5c0 4-5 9-5 9S0 9 0 5a5 5 0 0 1 5-5z" fill="#ddd"/></svg>18 Larkspur St, Hollowell</li>
    <li style="padding-left:33px">ACT 2611</li>
    <li><svg width="12" height="12" viewBox="0 0 24 24" style="margin-right:18px"><path fill="#ddd" d="M6.6 10.8a15 15 0 0 0 6.6 6.6l2.2-2.2c.3-.3.7-.4 1-.2 1.1.4 2.3.6 3.6.6.6 0 1 .4 1 1V20c0 .6-.4 1-1 1A17 17 0 0 1 3 4c0-.6.4-1 1-1h3.5c.6 0 1 .4 1 1 0 1.3.2 2.5.6 3.6.1.3 0 .7-.2 1z"/></svg>(02) 6140 0375</li>
    <li><svg width="13" height="10" viewBox="0 0 24 18" style="margin-right:17px"><rect width="24" height="18" rx="2" fill="#ddd"/></svg>info@kestrelviewaudits.com.au</li>
  </ul>
  <h3 class="abs foot-h" style="left:763px;top:3815px">Members</h3>
  <div class="abs badge" style="left:763px;top:3855px;width:124px;height:132px"></div>
  <div class="abs badge" style="left:905px;top:3870px;width:221px;height:90px;background:#1f8a3a"></div>
  <div class="abs" style="left:72px;top:4078px;width:1056px;height:1px;background:#2d2f33"></div>
  <p class="abs copy">Copyright © 2022. Company Name.&nbsp; All Right Reserved</p>
  <div class="abs social"><span></span><span></span><span></span><span></span><span></span></div>
</footer>

</body>
</html>
```